Business Card Design

we need a business card design and logo for a new cleaning company ,called brightwater cleaning Service,LLC .we provide cleaning services
Updates

i will also like to include the company's website in the business card   brightwatercleaningservice.example

Industry/Entity Type

Business

Contact Information for Business Card

Brightwater Cleaning Service,LLC
Marco Villanueva
Owner
marco@brightwatercleaningservice.example
Cell 555-318-7724
Office 555-374-6082

```html
<!DOCTYPE html>
<html lang="en">
<head>
<meta charset="utf-8">
<title>Brightwater Cleaning Service – Business Card</title>
<link rel="stylesheet" href="https://fonts.googleapis.com/css2?family=Open+Sans:wght@400;700;800&display=swap">
<style>
  :root {
    --backdrop: #d6d7d9;
    --lime-light: #c8de6e;
    --lime-dark: #acd136;
    --purple: #53318f;
    --ink: #111111;
    --icon-red: #b3151c;
    --white: #ffffff;
  }
  * { box-sizing: border-box; margin: 0; padding: 0; }
  html, body {
    width: 1200px; height: 1200px; overflow: hidden;
    background: var(--backdrop);
    font-family: "Open Sans", sans-serif;
  }
  .business-card {
    position: absolute; left: 123px; top: 326px;
    width: 954px; height: 542px;
    background: linear-gradient(90deg, var(--lime-light), var(--lime-dark));
    overflow: hidden;
  }
  .chevrons { position: absolute; left: 160px; top: 56px; }
  .brand {
    position: absolute; right: 54px; top: 52px;
    display: flex; align-items: center; gap: 18px;
  }
  .brand-square {
    width: 60px; height: 60px; background: var(--white);
  }
  .brand-name {
    color: var(--purple); font-weight: 800;
    font-size: 31px; line-height: 33px; text-transform: uppercase;
    letter-spacing: 0.5px;
  }
  .owner {
    position: absolute; left: 540px; width: 264px; top: 242px;
    text-align: center;
  }
  .owner-name { font-weight: 700; font-size: 27px; color: var(--ink); line-height: 34px; }
  .owner-role { font-size: 22px; color: var(--purple); line-height: 28px; }
  .contacts {
    position: absolute; left: 52px; top: 322px; list-style: none;
  }
  .contacts li {
    display: flex; align-items: center; gap: 10px;
    font-size: 23px; line-height: 31px; color: var(--ink);
  }
  .icon { width: 26px; height: 26px; flex: none; }
  .web-band {
    position: absolute; left: 0; bottom: 0; width: 100%; height: 94px;
    background: var(--purple);
    display: flex; align-items: center; justify-content: center; gap: 8px;
  }
  .web-band span { color: var(--white); font-size: 23px; }
</style>
</head>
<body>
  <main class="business-card">
    <svg class="chevrons" width="144" height="98" viewBox="0 0 144 98" aria-hidden="true">
      <g fill="#ffffff" fill-opacity="0.35">
        <polygon points="0,0 20,0 50,49 20,98 0,98 30,49"/>
        <polygon points="47,0 67,0 97,49 67,98 47,98 77,49"/>
        <polygon points="94,0 114,0 144,49 114,98 94,98 124,49"/>
      </g>
    </svg>

    <div class="brand">
      <div class="brand-square"></div>
      <div class="brand-name">Brightwater<br>Cleaning<br>Service</div>
    </div>

    <div class="owner">
      <p class="owner-name">MARCO VILLANUEVA</p>
      <p class="owner-role">Owner</p>
    </div>

    <ul class="contacts">
      <li>
        <svg class="icon" viewBox="0 0 26 26" aria-label="Cell">
          <circle cx="13" cy="13" r="13" fill="#fff"/>
          <rect x="9" y="5" width="8" height="16" rx="1.5" fill="var(--icon-red)"/>
          <rect x="10.5" y="7.5" width="5" height="6" fill="#fff"/>
        </svg>
        555-318-7724
      </li>
      <li>
        <svg class="icon" viewBox="0 0 26 26" aria-label="Office">
          <circle cx="13" cy="13" r="13" fill="#fff"/>
          <path d="M7 8c2-3 4-2 5 0l-2 2c1 3 3 5 6 6l2-2c2 1 3 3 0 5-6 1-12-5-11-11z" fill="var(--icon-red)"/>
        </svg>
        555-374-6082
      </li>
      <li>
        <svg class="icon" viewBox="0 0 26 26" aria-label="Email">
          <circle cx="13" cy="13" r="13" fill="#fff"/>
          <rect x="5" y="8" width="16" height="11" fill="var(--icon-red)"/>
          <polyline points="5,8 13,14 21,8" fill="none" stroke="#fff" stroke-width="1.5"/>
        </svg>
        marco@brightwatercleaningservice.example
      </li>
    </ul>

    <footer class="web-band">
      <svg class="icon" viewBox="0 0 26 26" aria-label="Website">
        <circle cx="13" cy="13" r="12" fill="#fff"/>
        <g fill="none" stroke="var(--icon-red)" stroke-width="1.6">
          <circle cx="13" cy="13" r="8"/>
          <ellipse cx="13" cy="13" rx="3.5" ry="8"/>
          <line x1="5" y1="13" x2="21" y2="13"/>
          <line x1="6.5" y1="9" x2="19.5" y2="9"/>
          <line x1="6.5" y1="17" x2="19.5" y2="17"/>
        </g>
      </svg>
      <span>www.brightwatercleaningservice.example</span>
    </footer>
  </main>
</body>
</html>
```